Stationery Design Project

We need letterhead and business cards designed for our consulting firm. Color scheme, mostly deep blue (see logo). We are a commercial consulting work out firm, nationwide (large loans, $10MM and up). Visit our website for more info.
Updates

Project Deadline Extended
Reason: Meeting tomorrow morning to make final final decision. Would like this project to stay open to be able to provide feed back and receive final edits and approve. Thank you!!!

Target Market(s)

High end investors

Industry/Entity Type

Business

Requirements
Must have
• Letterhead must have the logo and the address

4817 Larkmoor Avenue, Suite 210, San Diego, CA 92107
Nice to have
• It would be nice to incorporate a watermark of all or some portion of the logo on the letterhead, or at least for the 2nd sheets.

Maybe our phone number: 858.555.0174
and/or webiste: www.tollandridgecap.example
Should not have
• Target users and audience of this will be men so, frilly or whimsical type designs are not preferred.

```html
<!DOCTYPE html>
<html lang="en">
<head>
<meta charset="utf-8">
<title>Tolland Ridge Capital — Stationery</title>
<link href="https://fonts.googleapis.com/css2?family=Cinzel:wght@500&family=Arimo:wght@400&display=swap" rel="stylesheet">
<style>
  :root {
    --stage: #555555;
    --paper: #ffffff;
    --ink-grey: #6d6e70;
    --rule-grey: #7a7b7d;
    --text-dark: #3a3a3a;
    --brand-blue: #0a82c4;
    --watermark: #ececec;
  }
  html, body {
    margin: 0;
    padding: 0;
    width: 1200px;
    height: 900px;
    overflow: hidden;
    background: var(--stage);
  }
  .canvas {
    position: relative;
    width: 1200px;
    height: 900px;
    font-family: "Arimo", Arial, sans-serif;
  }
  .letterhead {
    position: absolute;
    left: 78px;
    top: 38px;
    width: 640px;
    height: 828px;
    background: var(--paper);
  }
  .letterhead__brand {
    position: absolute;
    right: 26px;
    top: 74px;
    text-align: right;
  }
  .brand-name {
    font-family: "Cinzel", Georgia, serif;
    font-weight: 500;
    color: var(--ink-grey);
    letter-spacing: 0.5px;
    margin: 0;
    white-space: nowrap;
  }
  .letterhead__brand .brand-name { font-size: 24px; }
  .letterhead__rule {
    position: absolute;
    left: 0;
    right: 0;
    top: 108px;
    height: 2px;
    background: var(--rule-grey);
  }
  .letterhead__watermark {
    position: absolute;
    left: 85px;
    top: 299px;
    width: 470px;
    height: 233px;
    background: var(--watermark);
  }
  .letterhead__footer {
    position: absolute;
    left: 21px;
    bottom: 21px;
    font-size: 10.5px;
    line-height: 15px;
    color: var(--text-dark);
  }
  .letterhead__band {
    position: absolute;
    left: 0;
    right: 0;
    bottom: 0;
    height: 13px;
    background: var(--brand-blue);
  }
  .card {
    position: absolute;
    left: 768px;
    width: 386px;
    height: 196px;
  }
  .card--front {
    top: 312px;
    background: var(--paper);
    display: flex;
    align-items: center;
    justify-content: center;
  }
  .card--front .brand-name { font-size: 26px; }
  .card--back {
    top: 516px;
    height: 192px;
    width: 380px;
    background: var(--brand-blue);
    color: #ffffff;
  }
  .card--back .brand-name {
    position: absolute;
    left: 176px;
    top: 62px;
    font-size: 14px;
    color: #ffffff;
  }
  .card__contact {
    position: absolute;
    left: 177px;
    top: 104px;
    font-size: 12px;
    line-height: 16px;
    margin: 0;
  }
</style>
</head>
<body>
<main class="canvas">
  <section class="letterhead" aria-label="Letterhead">
    <div class="letterhead__brand">
      <p class="brand-name">Tolland Ridge Capital</p>
    </div>
    <div class="letterhead__rule"></div>
    <div class="letterhead__watermark" role="img" aria-label="Faint watermark area for the company mark"></div>
    <address class="letterhead__footer" style="font-style:normal">
      4817 Larkmoor Avenue, Suite 210, San Diego, CA 92107, ph. : 858.555.0174<br>
      website: www.tollandridgecap.example
    </address>
    <div class="letterhead__band"></div>
  </section>

  <section class="card card--front" aria-label="Business card front">
    <p class="brand-name">Tolland Ridge Capital</p>
  </section>

  <section class="card card--back" aria-label="Business card back">
    <p class="brand-name">Tolland Ridge Capital</p>
    <address class="card__contact" style="font-style:normal">
      4817 Larkmoor Avenue, Suite 210,<br>
      San Diego, CA 92107,<br>
      ph. : 858.555.0174<br>
      website: www.tollandridgecap.example
    </address>
  </section>
</main>
</body>
</html>
```